Business Card Design for Occupational Medicine Start Up Company

We need to design a professional business card. We are a healthcare company providing occupational medicine services to blue collar industries. We are professional, efficient and high quality service providers.

Target Market(s)

Blue Collar Industry: Shipbuilding, Ports, Trucking Companies; The Executives and Safety Officers for these companies

Industry/Entity Type

Healthcare

Contact Information for Business Card

Logo, Name, Title, Email, Phone

Other font styles liked:
• Please match our Brand Guide

Requirements
Must have
• Our Company Colors and Logo

```html
<!DOCTYPE html>
<html lang="en">
<head>
<meta charset="utf-8">
<title>Crewline Clinics – Business Card</title>
<link rel="stylesheet" href="https://fonts.googleapis.com/css2?family=Montserrat:wght@400;500;700;800&display=swap">
<style>
  :root {
    --navy: #2b2a78;
    --navy-deep: #23226a;
    --sky: #2ba6de;
    --gold: #f4b534;
    --ink: #2a2a3a;
    --paper: #ffffff;
    --backdrop: #e9eaee;
  }
  * { box-sizing: border-box; margin: 0; padding: 0; }
  html, body {
    width: 1200px; height: 1186px; overflow: hidden;
    background: var(--backdrop);
    font-family: "Montserrat", sans-serif;
  }
  .sheet {
    width: 1200px; height: 1186px;
    display: flex; flex-direction: column; align-items: center; justify-content: center;
    gap: 34px;
  }
  .card {
    position: relative;
    width: 940px; height: 537px;
    border-radius: 30px;
    overflow: hidden;
    box-shadow: 0 10px 28px rgba(0,0,0,.14);
  }

  /* Front */
  .card--front { background: var(--navy); }
  .front-brand {
    position: absolute; left: 470px; top: 238px;
    display: flex; align-items: center; gap: 20px;
  }
  .brand-dot { width: 60px; height: 60px; border-radius: 50%; background: var(--paper); }
  .brand-name {
    font-weight: 700; font-size: 40px; letter-spacing: 1px; line-height: 1;
    color: var(--paper); text-transform: uppercase;
  }

  /* Back */
  .card--back { background: var(--paper); }
  .back-brand {
    position: absolute; right: 80px; top: 92px;
    display: flex; align-items: center; gap: 18px;
  }
  .back-brand .brand-dot { background: var(--navy); width: 54px; height: 54px; }
  .back-brand .brand-name { color: var(--navy); font-size: 38px; }

  .rule {
    position: absolute; left: 60px; right: 60px; top: 300px; height: 4px;
    background: linear-gradient(to right,
      var(--sky) 0 32%, var(--navy) 32% 66%, var(--gold) 66% 100%);
  }
  .person { position: absolute; left: 60px; top: 222px; }
  .person__name { font-weight: 800; font-size: 40px; color: var(--navy); line-height: 1.1; }
  .person__title { font-size: 22px; color: var(--ink); margin-top: 4px; }

  .address {
    position: absolute; right: 60px; top: 322px;
    font-size: 21px; color: var(--ink); line-height: 1.35; text-align: right;
  }
  .contacts { position: absolute; left: 60px; top: 340px; list-style: none; }
  .contacts li {
    display: flex; align-items: center; gap: 16px;
    font-size: 23px; color: var(--ink); line-height: 1.7;
  }
  .contacts svg { width: 18px; height: 18px; fill: var(--sky); flex: none; }
</style>
</head>
<body>
<main class="sheet">

  <section class="card card--front" aria-label="Card front">
    <div class="front-brand">
      <span class="brand-dot"></span>
      <span class="brand-name">Crewline Clinics</span>
    </div>
  </section>

  <section class="card card--back" aria-label="Card back">
    <div class="back-brand">
      <span class="brand-dot"></span>
      <span class="brand-name">Crewline Clinics</span>
    </div>

    <div class="person">
      <p class="person__name">Daniel Moore</p>
      <p class="person__title">CEO &amp; Founder</p>
    </div>

    <div class="rule"></div>

    <p class="address">418 Harbor View Rd, #112<br>Lakemont, OH 43990</p>

    <ul class="contacts">
      <li>
        <svg viewBox="0 0 24 24" aria-hidden="true"><path d="M6.6 10.8a15.5 15.5 0 0 0 6.6 6.6l2.2-2.2a1 1 0 0 1 1-.25 11.4 11.4 0 0 0 3.6.57 1 1 0 0 1 1 1V20a1 1 0 0 1-1 1A17 17 0 0 1 3 4a1 1 0 0 1 1-1h3.5a1 1 0 0 1 1 1c0 1.25.2 2.45.57 3.6a1 1 0 0 1-.25 1z"/></svg>
        800-555-0142
      </li>
      <li>
        <svg viewBox="0 0 24 24" aria-hidden="true"><path d="M2 5h20v14H2zm2 2v.5l8 5 8-5V7z"/></svg>
        info@crewlineclinics.com
      </li>
      <li>
        <svg viewBox="0 0 24 24" aria-hidden="true"><circle cx="12" cy="12" r="10"/></svg>
        www.crewlineclinics.com
      </li>
    </ul>
  </section>

</main>
</body>
</html>
```